Business Card Design Project

I am opening a skin care studio called Glow Haven by Marisol. I will be offering a wide range of unique and affordable skin services including facials, chemical peels, microdermabrasion treatments, body wraps, salt glows, all waxing and eye lash extensions. If the business cards depicts what I would like, this would lead to brochures, web design, signs, etc.
Updates

Project Deadline Extended
Reason: A request to extend deadline was requested. I will be more than happy to accommodate.

Industry/Entity Type

Business

Requirements
Nice to have
• facial features so prospective client clearly identifies what type of business this is. Not stuffy or boring "spa" looking graphics. I am focusing just on face, body, waxing, eyelashes. No massage or nails.

```html
<!DOCTYPE html>
<html lang="en">
<head>
<meta charset="utf-8">
<title>Glow Haven by Marisol — Business Card</title>
<link rel="stylesheet" href="https://fonts.googleapis.com/css2?family=Questrial&family=Archivo+Narrow:wght@400;500&display=swap">
<style>
  :root {
    --stage: #f4f4f4;
    --paper: #eeece8;
    --ink: #111111;
    --rose: #f29ac4;
    --blush: #f7cde0;
    --lilac: #c9b3e0;
    --violet: #7a4fa3;
    --teal: #1f9ba0;
    --peach: #f6b48f;
    --shadow: rgba(0, 0, 0, 0.12);
  }
  * { box-sizing: border-box; margin: 0; padding: 0; }
  html, body {
    width: 1200px;
    height: 1200px;
    overflow: hidden;
    background: var(--stage);
  }
  .canvas {
    position: relative;
    width: 1200px;
    height: 1200px;
  }
  .card {
    position: absolute;
    left: 120px;
    width: 960px;
    height: 548px;
    background: var(--paper);
    overflow: hidden;
    box-shadow: 0 6px 24px var(--shadow);
  }
  .card--front { top: 40px; }
  .card--back { top: 612px; }

  /* Front */
  .front-art {
    position: absolute;
    inset: 0;
    background:
      radial-gradient(ellipse 30% 40% at 82% 48%, var(--rose) 0%, rgba(242,154,196,0) 70%),
      radial-gradient(ellipse 18% 22% at 8% 14%, var(--teal) 0%, rgba(31,155,160,0) 70%),
      radial-gradient(ellipse 18% 22% at 86% 12%, var(--teal) 0%, rgba(31,155,160,0) 70%),
      radial-gradient(ellipse 40% 30% at 50% 95%, var(--lilac) 0%, rgba(201,179,224,0) 75%),
      radial-gradient(ellipse 25% 30% at 10% 55%, var(--peach) 0%, rgba(246,180,143,0) 70%),
      linear-gradient(180deg, var(--blush) 0%, var(--paper) 45%, var(--paper) 100%);
    opacity: 0.85;
  }
  .front-title {
    position: absolute;
    left: 96px;
    top: 172px;
    font-family: "Questrial", sans-serif;
    font-size: 80px;
    font-weight: 400;
    letter-spacing: 1px;
    color: var(--ink);
    line-height: 1;
  }
  .front-sub {
    position: absolute;
    left: 0;
    width: 960px;
    top: 268px;
    padding-right: 220px;
    text-align: center;
    font-family: "Questrial", sans-serif;
    font-size: 36px;
    color: var(--ink);
    line-height: 1;
  }

  /* Back */
  .back-art {
    position: absolute;
    left: 0;
    top: 0;
    width: 420px;
    height: 548px;
  }
  .appointment {
    position: absolute;
    left: 380px;
    top: 58px;
    font-family: "Archivo Narrow", sans-serif;
    font-weight: 500;
    color: var(--ink);
    font-size: 42px;
    line-height: 1;
  }
  .appointment__heading { margin-bottom: 28px; }
  .appointment__row { margin-bottom: 22px; white-space: pre; }
  .contact {
    position: absolute;
    right: 36px;
    bottom: 36px;
    text-align: right;
    font-family: "Archivo Narrow", sans-serif;
    font-weight: 500;
    color: var(--ink);
    font-size: 34px;
    line-height: 1.2;
  }
</style>
</head>
<body>
<main class="canvas">

  <section class="card card--front" aria-label="Card front">
    <div class="front-art" role="img" aria-label="Watercolour-style portrait of a woman's face in pink, violet and teal tones"></div>
    <h1 class="front-title">GLOW HAVEN</h1>
    <p class="front-sub">by marisol</p>
  </section>

  <section class="card card--back" aria-label="Card back">
    <svg class="back-art" viewBox="0 0 420 548" role="img" aria-label="Watercolour-style close-up of an eye and cheek in violet, pink and teal tones">
      <defs>
        <linearGradient id="eyeArea" x1="0" y1="0" x2="1" y2="1">
          <stop offset="0" stop-color="#a57cc4"/>
          <stop offset="0.35" stop-color="#e58bb8"/>
          <stop offset="0.6" stop-color="#f3b89c"/>
          <stop offset="1" stop-color="#f4d6e4"/>
        </linearGradient>
        <radialGradient id="eyeTone" cx="0.3" cy="0.55" r="0.3">
          <stop offset="0" stop-color="#1f9ba0" stop-opacity="0.8"/>
          <stop offset="1" stop-color="#1f9ba0" stop-opacity="0"/>
        </radialGradient>
      </defs>
      <path d="M0 0 H150 C230 40 300 140 330 260 C360 370 350 470 300 548 H0 Z" fill="url(#eyeArea)" opacity="0.9"/>
      <path d="M0 0 H150 C230 40 300 140 330 260 C360 370 350 470 300 548 H0 Z" fill="url(#eyeTone)"/>
    </svg>

    <div class="appointment">
      <p class="appointment__heading">APPOINTMENT</p>
      <p class="appointment__row">DATE ....\....\.....</p>
      <p class="appointment__row">TIME  ....:.....</p>
    </div>

    <address class="contact" style="font-style: normal;">
      <p>412 Cedar Avenue Fairview, CO 80999</p>
      <p>555-014-2273</p>
      <p>glowhavenbymarisol.com</p>
    </address>
  </section>

</main>
</body>
</html>
```